Holvern Incorporated

Holvern is a business that provides consulting, and manages and supplies trades persons in the construction and heavy industries sector. We build, do maintenance, install machinery, and can manage projects or jobs. Would like or prefer more clean, classic designs. Blacks/greys, but open to almost anything.

Target Market(s)

Industrial/Construction/Manufacturing

Industry/Entity Type

Construction Company

Contact Information for Business Card

Clean, business name on the front, possibly have the details on the back, but open to any ideas.

Logo Text

We currently do not have a slogan, open to ideas

Font styles to use
Serif
Sans Serif

Colors

Designer to choose colors to be used in the design.

Requirements
Should not have
• the oval is not my logo, was just an idea. please don't send 20 designs with the oval

```html
<!DOCTYPE html>
<html lang="en">
<head>
<meta charset="utf-8">
<title>Holvern Incorporated – Business Card</title>
<link href="https://fonts.googleapis.com/css2?family=Open+Sans:wght@400;700&display=swap" rel="stylesheet">
<style>
  :root {
    --page-bg: #e6e4e1;
    --card-bg: #2a2a2a;
    --card-shadow: rgba(0, 0, 0, 0.28);
    --text-light: #f2f2f2;
    --text-muted: #d6d6d6;
    --logo-tone: #4a4a4a;
    --rule: #bdbdbd;
  }
  * { box-sizing: border-box; margin: 0; padding: 0; }
  html, body {
    width: 1200px;
    height: 900px;
    overflow: hidden;
    background: var(--page-bg);
    font-family: "Open Sans", Arial, sans-serif;
  }
  .canvas {
    position: relative;
    width: 1200px;
    height: 900px;
  }
  .card {
    position: absolute;
    left: 280px;
    width: 640px;
    height: 366px;
    background: var(--card-bg);
    box-shadow: 0 10px 28px var(--card-shadow);
  }
  .card--front { top: 70px; }
  .card--back { top: 464px; }

  .brand {
    position: absolute;
    inset: 0;
    display: flex;
    align-items: center;
    justify-content: center;
    gap: 14px;
  }
  .brand__mark {
    width: 14px;
    height: 14px;
    background: var(--logo-tone);
  }
  .brand__name {
    font-size: 46px;
    font-weight: 700;
    letter-spacing: 1px;
    color: var(--logo-tone);
    line-height: 1;
  }
  .brand__name small {
    font-size: 46px;
    font-weight: 700;
  }

  .identity {
    position: absolute;
    right: 340px;
    top: 162px;
    text-align: right;
    color: var(--text-light);
  }
  .identity__name {
    font-size: 22px;
    font-weight: 700;
    letter-spacing: 0.5px;
    line-height: 1.1;
  }
  .identity__role {
    font-size: 15px;
    font-weight: 400;
    color: var(--text-muted);
    margin-top: 2px;
  }
  .divider {
    position: absolute;
    left: 316px;
    top: 150px;
    width: 1px;
    height: 82px;
    background: var(--rule);
  }
  .contacts {
    position: absolute;
    left: 330px;
    top: 152px;
    list-style: none;
    color: var(--text-light);
    font-size: 15px;
    line-height: 26px;
  }
  .contacts li {
    display: flex;
    align-items: center;
    gap: 6px;
  }
  .contacts svg {
    width: 12px;
    height: 12px;
    fill: var(--text-light);
    flex: none;
  }
  .address {
    position: absolute;
    left: 230px;
    top: 300px;
    color: var(--text-light);
    font-size: 15px;
  }
</style>
</head>
<body>
<main class="canvas">
  <section class="card card--front" aria-label="Card front">
    <div class="brand">
      <span class="brand__mark"></span>
      <span class="brand__name">Holvern Incorporated</span>
    </div>
  </section>

  <section class="card card--back" aria-label="Card back">
    <div class="identity">
      <p class="identity__name">DALE WARRICK</p>
      <p class="identity__role">President</p>
    </div>
    <span class="divider"></span>
    <ul class="contacts">
      <li>
        <svg viewBox="0 0 16 16" aria-hidden="true"><path d="M3.6 1.2l2.3 2.3c.4.4.4 1 0 1.4L4.7 6.1c.8 1.9 3.3 4.4 5.2 5.2l1.2-1.2c.4-.4 1-.4 1.4 0l2.3 2.3c.4.4.4 1 0 1.4l-1.3 1.3C10.8 16.6 -.6 5.2 .9 2.5L2.2 1.2c.4-.4 1-.4 1.4 0z"/></svg>
        555-318-0472
      </li>
      <li>
        <svg viewBox="0 0 16 16" aria-hidden="true"><path d="M1 3h14v1.2L8 9 1 4.2z M1 6l7 4.8L15 6v7H1z"/></svg>
        info@holvern.com
      </li>
      <li>
        <svg viewBox="0 0 16 16" aria-hidden="true"><circle cx="8" cy="8" r="7"/></svg>
        www.holvern.com
      </li>
    </ul>
    <p class="address">1180 Harbor Ridge Road, Port Elwin CA 90000</p>
  </section>
</main>
</body>
</html>
```